Front Yard Sign for Real Estate Company

Bright Porch Keys is a brand new real estate broker. We need signs to put in front yard of houses that we are selling. 3D would be great. I have included the company LOGO

Target Market(s)

Residential Property buyers and sellers

Industry/Entity Type

Real Estate

Colors
ec1f27
ffc214
fbed22
ffffff

Requirements
Must have
• 3D look would be great. Logo must be included in the yard signs.
• Must include phone # to call: 614-290-4417

```html
<!DOCTYPE html>
<html lang="en">
<head>
<meta charset="utf-8">
<title>Bright Porch Keys – Yard Sign</title>
<link href="https://fonts.googleapis.com/css2?family=Anton&family=Archivo+Black&family=Montserrat:ital,wght@0,800;1,500&display=swap" rel="stylesheet">
<style>
  :root {
    --brand-red: #ec1f27;
    --brand-gold: #ffc214;
    --brand-yellow: #fbed22;
    --white: #ffffff;
    --backdrop: #eceef0;
    --shadow: rgba(0,0,0,0.22);
    --band-shadow: #d8d8d8;
  }
  html, body {
    margin: 0;
    padding: 0;
    width: 1200px;
    height: 1200px;
    overflow: hidden;
    background: var(--backdrop);
  }
  .canvas {
    position: relative;
    width: 1200px;
    height: 1200px;
  }
  .yard-sign {
    position: absolute;
    left: 205px;
    top: 43px;
    width: 790px;
    height: 1114px;
    background: var(--white);
    overflow: hidden;
    box-shadow: 0 14px 36px var(--shadow);
  }
  .sign-bands {
    position: absolute;
    inset: 0;
    width: 790px;
    height: 1114px;
  }
  .brand-name {
    position: absolute;
    top: 200px;
    left: 0;
    width: 790px;
    margin: 0;
    text-align: center;
    font-family: "Montserrat", sans-serif;
    font-weight: 800;
    font-size: 56px;
    letter-spacing: -1.5px;
    color: var(--brand-red);
    line-height: 1;
  }
  .tagline {
    position: absolute;
    top: 290px;
    left: 0;
    width: 790px;
    display: flex;
    align-items: center;
    justify-content: center;
    gap: 14px;
    font-family: "Montserrat", sans-serif;
    font-style: italic;
    font-weight: 500;
    font-size: 25px;
    line-height: 1.1;
    color: var(--brand-red);
  }
  .tagline .rule {
    width: 60px;
    height: 2px;
    background: var(--brand-gold);
  }
  .headline-for {
    position: absolute;
    top: 478px;
    left: 0;
    width: 790px;
    display: flex;
    align-items: center;
    justify-content: center;
    gap: 18px;
    font-family: "Anton", sans-serif;
    font-size: 104px;
    line-height: 1;
    color: var(--brand-red);
    text-shadow: 4px 5px 6px var(--shadow);
  }
  .headline-for .rule {
    width: 150px;
    height: 22px;
    background: var(--brand-red);
    box-shadow: 3px 4px 5px var(--shadow);
  }
  .headline-sell {
    position: absolute;
    top: 575px;
    left: 0;
    width: 790px;
    margin: 0;
    text-align: center;
    font-family: "Anton", sans-serif;
    font-size: 228px;
    line-height: 1;
    letter-spacing: 2px;
    color: var(--brand-red);
    text-shadow: 6px 8px 8px var(--shadow);
  }
  .call-label {
    position: absolute;
    top: 918px;
    left: 0;
    width: 790px;
    display: flex;
    align-items: center;
    justify-content: center;
    gap: 12px;
    font-family: "Archivo Black", sans-serif;
    font-size: 42px;
    line-height: 1;
    color: var(--white);
  }
  .call-label .rule {
    width: 150px;
    height: 5px;
    background: var(--white);
  }
  .phone-pill {
    position: absolute;
    top: 976px;
    left: 50px;
    width: 690px;
    height: 94px;
    border-radius: 47px;
    background: var(--brand-yellow);
    display: flex;
    align-items: center;
    justify-content: center;
    font-family: "Archivo Black", sans-serif;
    font-size: 72px;
    letter-spacing: 1px;
    color: var(--brand-red);
  }
</style>
</head>
<body>
<main class="canvas">
  <section class="yard-sign">
    <svg class="sign-bands" viewBox="0 0 790 1114" aria-hidden="true">
      <path d="M0,392 C250,480 600,460 790,300 L790,308 C600,472 250,492 0,400 Z" fill="var(--band-shadow)"/>
      <path d="M0,345 C250,425 600,405 790,262 L790,300 C600,460 250,480 0,392 Z" fill="var(--brand-yellow)"/>
      <path d="M560,412 Q700,385 790,262 L790,412 Z" fill="var(--brand-red)"/>
      <path d="M0,822 Q380,760 790,948 L790,972 Q380,800 0,868 Z" fill="var(--brand-yellow)"/>
      <path d="M0,868 Q380,800 790,972 L790,1114 L0,1114 Z" fill="var(--brand-red)"/>
    </svg>

    <h1 class="brand-name">Bright Porch Keys</h1>
    <div class="tagline"><span class="rule"></span><span>Your Key Home, Made Simple</span><span class="rule"></span></div>

    <div class="headline-for"><span class="rule"></span><span>FOR</span><span class="rule"></span></div>
    <h2 class="headline-sell">SELL</h2>

    <div class="call-label"><span class="rule"></span><span>CALL</span><span class="rule"></span></div>
    <div class="phone-pill">614-290-4417</div>
  </section>
</main>
</body>
</html>
```